Book Cover for: TITLE Mend the Quiet Tide SUBTITLE For couples who don't want to break up

We need a full cover design for a book on relationships written by husband and wife team, Marla and Dennis Holtwick, PhD. This book will offer hope for couples that are on the verge of breaking up but want to work things out and stay together. The theme is to teach couples about their own reactions to their partner, how moods affect a relationship, how to get creative to solving problems and how to have a good feeling towards your partner regardless of differences. This book is about hope. It is a positive look at relationships that feel hopeless.

Target Market(s)

Married or couples that are going through a difficult time and are considering splitting up due to, communication difficulties, addiction, affair. We imagine the book will appeal to women more than men but still want a cover that men would be comfortable picking up.

Colors

Designer to choose colors to be used in the design.

Requirements
Must have
• We want the cover to beautiful, intriguing, simple and uncomplicated. We don't want it overly busy, technical, or complex.
Nice to have
• MAYBE?? a broken heart being put back together.
Should not have
• No photo, no cartoon, no flowers, no couple (unless obscure and not gender specific).

```html
<!DOCTYPE html>
<html lang="en">
<head>
<meta charset="utf-8">
<title>Mend the Quiet Tide — Full Cover</title>
<link rel="stylesheet" href="https://fonts.googleapis.com/css2?family=Bodoni+Moda:wght@400;500&family=Allura&family=Montserrat:wght@700&family=Poppins:wght@300;500&display=swap">
<style>
  :root {
    --stage: #c4005a;
    --paper: #ebe9e6;
    --paper-soft: #e2dfdb;
    --ink: #2b2b2d;
    --rose: #e6126b;
    --rose-deep: #c90858;
    --band-white: #ffffff;
    --bandage: #2f3445;
  }
  * { box-sizing: border-box; margin: 0; padding: 0; }
  html, body {
    width: 1200px; height: 848px; overflow: hidden;
    background: var(--stage);
  }
  .spread {
    position: absolute; left: 20px; top: 31px;
    width: 1160px; height: 786px;
    background: var(--paper);
    overflow: hidden;
  }
  .back, .spine, .front { position: absolute; top: 0; height: 100%; }
  .back { left: 0; width: 563px; }
  .spine { left: 563px; width: 56px; }
  .front { left: 619px; width: 541px; }

  /* Title lockup */
  .title { position: absolute; text-align: center; color: var(--ink); }
  .title .word {
    display: block;
    font-family: "Bodoni Moda", serif; font-weight: 400;
    letter-spacing: -0.02em; line-height: 1;
  }
  .title .script {
    display: block;
    font-family: "Allura", cursive; color: var(--rose);
    line-height: 0.6; position: relative; z-index: 1;
  }
  .title--front { left: 106px; top: 336px; width: 360px; }
  .title--front .word { font-size: 72px; }
  .title--front .script { font-size: 96px; margin: -8px 0 6px; }
  .title--back { left: 200px; top: 50px; width: 180px; }
  .title--back .word { font-size: 32px; }
  .title--back .script { font-size: 44px; margin: -4px 0 2px; }

  .subtitle {
    position: absolute; left: 106px; top: 580px; width: 360px;
    text-align: center;
    font-family: "Montserrat", sans-serif; font-weight: 700;
    font-size: 14.5px; line-height: 1.25; color: var(--rose-deep);
    text-transform: uppercase; letter-spacing: 0.01em;
  }
  .authors {
    position: absolute; left: 40px; top: 694px; width: 492px;
    text-align: center;
    font-family: "Bodoni Moda", serif; font-size: 29px;
    color: var(--rose-deep); text-transform: uppercase; letter-spacing: 0.01em;
  }
  .heart-art {
    position: absolute; left: 123px; top: 80px; width: 312px; height: 232px;
    border-radius: 46% 46% 50% 50% / 40% 40% 60% 60%;
    background: radial-gradient(circle at 40% 40%, #ff3d8e, var(--rose-deep) 70%);
  }

  /* Spine */
  .spine-title, .spine-authors {
    position: absolute; left: 0; width: 56px;
    writing-mode: vertical-rl;
    display: flex; align-items: center;
    font-family: "Bodoni Moda", serif; text-transform: uppercase;
    font-size: 24px; letter-spacing: 0.01em; white-space: nowrap;
  }
  .spine-title { top: 54px; color: var(--rose); }
  .spine-authors { top: 420px; color: var(--ink); }

  /* Back copy */
  .back-heading {
    position: absolute; left: 81px; top: 155px;
    font-family: "Poppins", sans-serif; font-weight: 500;
    font-size: 13px; color: var(--rose);
  }
  .copy {
    position: absolute; left: 81px; width: 432px;
    font-family: "Poppins", sans-serif; font-weight: 300;
    font-size: 12.2px; line-height: 15.8px; color: var(--ink);
    text-align: justify;
  }
  .copy p { text-indent: 10px; }
  .copy--intro { top: 188px; }
  .copy--approach { top: 296px; }
  .copy--more { top: 606px; }
  .authors-band {
    position: absolute; left: 0; top: 416px; width: 563px; height: 178px;
    background: linear-gradient(90deg, var(--paper) 0%, #e55a94 40%, var(--rose) 78%, #f6bcd3 100%);
  }
  .authors-band .copy {
    top: 30px; color: var(--band-white); font-weight: 300;
  }
</style>
</head>
<body>
  <main class="spread">
    <section class="back">
      <div class="title title--back">
        <span class="word">MEND</span>
        <span class="script">the quiet</span>
        <span class="word">TIDE</span>
      </div>
      <h2 class="back-heading">About the book</h2>
      <div class="copy copy--intro">
        <p>Have you ever wondered how you can go from being so deeply in love with your partner to finding yourself miserable in your relationship? What happened? This book sheds light on that question and the human dilemma around relationships. Marla and Dennis Holtwick Ph.D. have been married for forty-five years and found their way out of their own troubled relationship.</p>
      </div>
      <div class="copy copy--approach">
        <p>In this book, they propose a new approach that helps you live more gracefully with your partner, without needing to put issues to rest first. It points to a deeper relationship with yourself and each other. Told in easy, digestible chapters and true stories, this book has the potential to lead to lasting change.</p>
      </div>
      <div class="authors-band">
        <div class="copy">
          <p>Marla and Dennis have spent decades working with couples around the world and in their home state. They are founders of a non-profit educational organization offering counseling services for couples and relationship training for professionals. Their objective for each couple is to restore hope and goodwill, not to fix things logistically.</p>
        </div>
      </div>
      <div class="copy copy--more">
        <p>Much of the pain in couples is attributed to habits of thought and interaction, not to flaws in partners or interpersonal skill. Through talks, recordings and sessions, the distance between you can close. Their Relationship Handbook, offers the same positive shifts that couples describe. Learn more at quiettidecouples.org</p>
      </div>
    </section>

    <section class="spine">
      <div class="spine-title">Mend the Quiet Tide</div>
      <div class="spine-authors">Marla &amp; Dennis Holtwick</div>
    </section>

    <section class="front">
      <div class="heart-art" role="img" aria-label="Cracked pink heart held together by a dark bandage"></div>
      <h1 class="title title--front">
        <span class="word">MEND</span>
        <span class="script">the quiet</span>
        <span class="word">TIDE</span>
      </h1>
      <p class="subtitle">For couples who don't want<br>to break up</p>
      <p class="authors">Marla &amp; Dennis Holtwick</p>
    </section>
  </main>
</body>
</html>
```